[WEB DESIGN - Start-up] Online LOANS against Luxury Assets - Needs a Web Design

Hello,
We need a web design for a new company. We make online LOANS against Luxury assets.
The name is private, that's why you could remplace it by the term "LOGO" or "ENTERPRISE".

In attachments, you'll find few models that we would like. Nonetheless, we don't want a copy of these screenshots. They are only prototypes that we made. Here we expect you to lead a professional web Design with your intuition and your ideas.

The final design should communicate start-up spirit, professionalism and fluidity.

Best Regards.

Industry/Entity Type

Finance

Number of Pages Required

2 page

Font styles to use
Sans Serif

Colors
f78f20
ffffff
b2b2b2
e9e9e9

Requirements
Must have
• The designer will draw on the 2015 web trends.
• The subject site is serious (loans against luxury assets), but the site should be modern and pleasant.
• PLEASE REFER YOU TO MY MODEL ( ATTACHMENTS)
Nice to have
• Surprise-me ! Welcome to a lot of imagination.

```html
<!DOCTYPE html>
<html lang="fr">
<head>
<meta charset="utf-8">
<title>Lumen Loans</title>
<link href="https://fonts.googleapis.com/css2?family=Cinzel:wght@400;700&family=Open+Sans:wght@400;600;700&display=swap" rel="stylesheet">
<style>
:root{
  --orange:#f78f20;
  --white:#ffffff;
  --grey:#b2b2b2;
  --light:#e9e9e9;
  --darker:#0c0c0c;
  --text:#555555;
}
*{box-sizing:border-box;margin:0;padding:0}
html,body{width:1200px;height:2808px;overflow:hidden}
body{font-family:"Open Sans",Arial,sans-serif;color:var(--text);background:var(--white);font-size:13px;line-height:1.5}
.title{font-family:"Cinzel",Georgia,serif;font-weight:400;letter-spacing:1px}
.brand{font-family:"Open Sans",Arial,sans-serif;font-weight:600;color:var(--white);font-size:26px;display:flex;align-items:center;gap:10px}
.brand::before{content:"";width:14px;height:14px;background:var(--orange)}

/* hero */
.hero{position:relative;height:520px;background:radial-gradient(ellipse at 50% 30%,#3b3b3b 0%,#161616 70%)}
.hero-visual-left{position:absolute;left:0;top:60px;width:360px;height:260px;background:radial-gradient(ellipse at 40% 50%,#6b6b6b,rgba(30,30,30,0) 70%)}
.hero-visual-right{position:absolute;right:0;top:160px;width:400px;height:300px;background:radial-gradient(ellipse at 60% 50%,#6f6a55,rgba(30,30,30,0) 70%)}
.topbar{position:relative;height:64px;display:flex;align-items:center;justify-content:space-between;padding:0 70px 0 50px;background:rgba(0,0,0,.55)}
.nav{display:flex;gap:42px;list-style:none}
.nav li{font-size:12px;color:var(--white);text-transform:uppercase}
.nav li.active{color:var(--orange);border-bottom:2px solid var(--orange);padding-bottom:4px}
.hero-title{position:relative;text-align:center;color:var(--white);font-size:34px;margin-top:12px}
.search{position:absolute;left:320px;top:335px;width:530px;background:rgba(20,20,20,.85);padding:14px 18px 18px;border-top:3px solid var(--orange)}
.search h3{color:var(--orange);font-size:13px;font-weight:600;text-transform:uppercase;margin-bottom:10px}
.search-row{display:flex;gap:10px;margin-bottom:10px}
.field{flex:1;height:28px;background:#2a2a2a;border:1px solid #444;color:var(--grey);font-size:11px;display:flex;align-items:center;padding:0 10px}
.field.btn{flex:0 0 110px;background:var(--orange);color:var(--white);justify-content:center;font-weight:600}
.dots{display:flex;gap:8px;justify-content:center}
.dots span{width:10px;height:10px;border-radius:50%;background:var(--grey)}
.dots span.on{background:var(--white)}
.hero .dots{position:absolute;left:0;right:0;top:488px}

/* steps */
.steps{height:390px;background:var(--white);position:relative}
.steps-band{position:absolute;left:0;right:0;top:92px;height:34px;background:var(--light)}
.step-list{position:relative;display:flex;justify-content:center;gap:40px;padding-top:28px}
.step{width:220px}
.step-circle{width:150px;height:150px;margin:0 auto 18px;border-radius:50%;border:6px solid var(--orange);background:var(--white);display:flex;align-items:center;justify-content:center;box-shadow:0 0 0 6px var(--light)}
.step h4{font-size:16px;font-weight:700;color:#222;text-align:center;letter-spacing:1px;margin-bottom:8px}
.step p{font-size:11px;color:#777;padding:0 12px}

/* assets */
.assets{height:890px;background:linear-gradient(#1a1a1a,#0e0e0e);padding-top:26px}
.assets h2{text-align:center;color:var(--white);font-size:30px;margin-bottom:22px}
.asset-grid{width:940px;margin:0 auto;display:grid;grid-template-columns:repeat(4,1fr);gap:8px}
.asset{height:240px;position:relative;display:flex;align-items:flex-end;justify-content:center}
.asset span{position:relative;color:var(--white);font-size:13px;font-weight:600;text-transform:uppercase;padding-bottom:14px;text-shadow:0 1px 3px #000}
.asset .photo{position:absolute;inset:0}
.assets .dots{margin-top:16px;justify-content:flex-end;padding-right:130px}

/* help */
.help{height:250px;background:var(--white);padding-top:24px;text-align:center}
.help h2{color:var(--orange);font-size:26px;margin-bottom:20px}
.help-cols{display:flex;justify-content:center}
.help-col{width:300px;padding:0 20px;border-left:1px solid var(--light)}
.help-col:first-child{border-left:none}
.help-col svg{display:block;margin:0 auto 10px}
.help-col small{display:block;color:var(--grey);font-size:12px}
.help-col strong{display:block;color:var(--orange);font-size:18px;font-weight:600}
.help-col a{color:var(--orange);text-decoration:none;font-weight:600;font-size:13px;display:block}

/* stats */
.trust{height:80px;background:var(--light);display:flex;align-items:center;justify-content:center}
.trust h2{color:var(--orange);font-size:26px}
.proof{height:290px;background:var(--light);display:flex;gap:40px;padding:0 90px 0 125px}
.testimonials{width:530px;height:260px;background:var(--white);padding:16px 26px;box-shadow:0 2px 6px rgba(0,0,0,.1)}
.testimonials h3,.figures h3{font-size:20px;font-weight:400;color:#333;margin-bottom:14px}
.figures h3{color:var(--orange)}
.quote{display:flex;gap:24px}
.avatar{width:120px;height:120px;flex:none;background:linear-gradient(#c8c8c8,#9a9a9a)}
.quote p{font-size:11px;color:#777}
.quote cite{display:block;font-style:normal;color:var(--orange);font-size:12px;margin-top:8px}
.testimonials .dots{justify-content:flex-end;margin-top:26px}
.figures{flex:1;padding-top:16px}
.figures p{font-size:11px;color:#777;margin-bottom:18px}
.counter{display:flex;gap:4px;margin-bottom:14px}
.counter span{width:30px;height:42px;background:#222;color:var(--white);font-size:26px;font-weight:700;display:flex;align-items:center;justify-content:center;border-radius:3px}

/* footer */
.footer{height:388px;background:var(--darker);color:var(--grey);display:flex;padding:40px 90px 0 125px;gap:60px;position:relative}
.footer h3{color:var(--white);font-size:20px;margin-bottom:12px}
.footer-about{width:330px;font-size:11px}
.footer-links{list-style:none;font-size:11px;line-height:1.9;width:150px}
.footer-contact{font-size:11px;display:flex;gap:12px;width:330px}
.footer .brand{position:absolute;right:100px;top:270px;font-size:30px}
.copyright{position:absolute;left:0;right:0;bottom:14px;text-align:center;font-size:10px;color:#777}
</style>
</head>
<body>

<header class="hero">
  <div class="hero-visual-left" role="img" aria-label="Main tenant un diamant à la pince"></div>
  <div class="hero-visual-right" role="img" aria-label="Mains échangeant des billets de banque"></div>
  <div class="topbar">
    <div class="brand">Lumen Loans</div>
    <ul class="nav">
      <li class="active">Accueil</li><li>Concept</li><li>Les Biens</li><li>Estimations</li><li>FAQ</li><li>Mon Compte</li>
    </ul>
  </div>
  <h1 class="hero-title title">On Se Lasse De Tout, Sauf De L'Argent.</h1>
  <form class="search">
    <h3>Demande de crédit</h3>
    <div class="search-row"><div class="field">Catégorie</div><div class="field">Valeur estimée du bien</div></div>
    <div class="search-row"><div class="field">Prix souhaité</div><div class="field btn">Estimer</div></div>
  </form>
  <div class="dots"><span class="on"></span><span></span><span></span></div>
</header>

<section class="steps">
  <div class="steps-band"></div>
  <div class="step-list">
    <div class="step">
      <div class="step-circle"><svg width="60" height="60" viewBox="0 0 60 60"><circle cx="30" cy="30" r="22" fill="none" stroke="#f78f20" stroke-width="4"/><text x="30" y="40" text-anchor="middle" font-size="28" font-weight="700" fill="#f78f20" font-family="Open Sans,sans-serif">$</text></svg></div>
      <h4>ESTIMATION</h4>
      <p>Lorem ipsum dolor sit amet, ex vim ipsum primis. Sed quaestio molestiae ea duo, fabellas eleifend ut usu, ei labore feugiat vim.</p>
    </div>
    <div class="step">
      <div class="step-circle"><svg width="60" height="60" viewBox="0 0 60 60"><path d="M14 36 L30 24 L46 36 L46 48 L14 48 Z" fill="none" stroke="#f78f20" stroke-width="4"/><circle cx="30" cy="14" r="7" fill="#f78f20"/></svg></div>
      <h4>PAIEMENT</h4>
      <p>Lorem ipsum dolor sit amet, ex vim ipsum primis. Sed quaestio molestiae ea duo, fabellas eleifend ut usu, ei labore feugiat vim.</p>
    </div>
    <div class="step">
      <div class="step-circle"><svg width="60" height="60" viewBox="0 0 60 60"><g fill="none" stroke="#f78f20" stroke-width="4"><ellipse cx="26" cy="16" rx="14" ry="5"/><path d="M12 16v22c0 3 6 5 14 5s14-2 14-5V16"/><path d="M12 27c0 3 6 5 14 5s14-2 14-5"/></g><rect x="38" y="34" width="14" height="12" fill="#f78f20"/></svg></div>
      <h4>SECURISATION</h4>
      <p>Lorem ipsum dolor sit amet, ex vim ipsum primis. Sed quaestio molestiae ea duo, fabellas eleifend ut usu, ei labore feugiat vim.</p>
    </div>
    <div class="step">
      <div class="step-circle"><svg width="60" height="60" viewBox="0 0 60 60"><rect x="10" y="18" width="40" height="26" fill="none" stroke="#f78f20" stroke-width="4"/><text x="30" y="38" text-anchor="middle" font-size="18" font-weight="700" fill="#f78f20" font-family="Open Sans,sans-serif">$</text></svg></div>
      <h4>RACHAT</h4>
      <p>Lorem ipsum dolor sit amet, ex vim ipsum primis. Sed quaestio molestiae ea duo, fabellas eleifend ut usu, ei labore feugiat vim.</p>
    </div>
  </div>
</section>

<section class="assets">
  <h2 class="title">Les Biens Que Nous Acceptons</h2>
  <div class="asset-grid">
    <div class="asset"><div class="photo" role="img" aria-label="Instrument de musique" style="background:linear-gradient(#5a3a22,#1c120a)"></div><span>Instrument</span></div>
    <div class="asset"><div class="photo" role="img" aria-label="Galerie de tableaux" style="background:linear-gradient(#c9b79a,#6e5a44)"></div><span>Art - Tableaux</span></div>
    <div class="asset"><div class="photo" role="img" aria-label="Pierres précieuses" style="background:linear-gradient(#6a5aa0,#1d1630)"></div><span>Pierres Précieuses</span></div>
    <div class="asset"><div class="photo" role="img" aria-label="Bouteilles de vin" style="background:linear-gradient(#5b1f1a,#140606)"></div><span>Vins &amp; Spiritueux</span></div>
    <div class="asset"><div class="photo" role="img" aria-label="Vase en porcelaine" style="background:linear-gradient(#dfe3ea,#2a3f7a)"></div><span>Art - Sculptures</span></div>
    <div class="asset"><div class="photo" role="img" aria-label="Matériel professionnel" style="background:linear-gradient(#4f6b50,#a07a3e)"></div><span>Mat Profes</span></div>
    <div class="asset"><div class="photo" role="img" aria-label="Bijoux en or" style="background:linear-gradient(#c89a3a,#5b3e12)"></div><span>Bijoux</span></div>
    <div class="asset"><div class="photo" role="img" aria-label="Montre de luxe" style="background:linear-gradient(#8a8a8a,#2a2a2a)"></div><span>Montres</span></div>
    <div class="asset"><div class="photo" role="img" aria-label="Voiture de collection" style="background:linear-gradient(#3a4a5a,#12161c)"></div><span>Véhicules</span></div>
    <div class="asset"><div class="photo" role="img" aria-label="Lingots d'or" style="background:linear-gradient(#d9a640,#6b4512)"></div><span>Métaux Précieux</span></div>
    <div class="asset"><div class="photo" role="img" aria-label="Sac de maroquinerie" style="background:linear-gradient(#6b4428,#24160c)"></div><span>Maroquinerie</span></div>
    <div class="asset"><div class="photo" role="img" aria-label="Appareils high-tech" style="background:linear-gradient(#9ea4aa,#2c3034)"></div><span>High-Tech</span></div>
  </div>
  <div class="dots"><span class="on"></span><span></span><span></span></div>
</section>

<section class="help">
  <h2 class="title">Besoin D'aide? Nous Sommes À Votre Écoute</h2>
  <div class="help-cols">
    <div class="help-col">
      <svg width="42" height="60" viewBox="0 0 50 70"><rect x="6" y="2" width="38" height="66" rx="6" fill="#222"/><rect x="11" y="10" width="28" height="46" fill="#fff"/><circle cx="25" cy="62" r="3" fill="#fff"/></svg>
      <small>Du lundi au vendredi de 9h à 19h</small>
      <strong>01 23 45 67 89</strong>
    </div>
    <div class="help-col">
      <svg width="52" height="60" viewBox="0 0 60 70"><circle cx="30" cy="18" r="14" fill="#222"/><path d="M4 68c0-18 12-30 26-30s26 12 26 30Z" fill="#222"/></svg>
      <a>Questions<br>Fréquentes</a>
    </div>
    <div class="help-col">
      <svg width="70" height="52" viewBox="0 0 80 60"><rect x="2" y="6" width="76" height="50" fill="#222"/><path d="M4 8 L40 36 L76 8" fill="none" stroke="#fff" stroke-width="4"/></svg>
      <a>Formulaire de contact</a>
      <small>ou</small>
      <a>contact@lumenloans.example</a>
    </div>
  </div>
</section>

<div class="trust"><h2 class="title">Entreprise EST N1 De La Vente Avec Faculté De Rachat</h2></div>

<section class="proof">
  <div class="testimonials">
    <h3>Derniers Témoignages</h3>
    <div class="quote">
      <div class="avatar" role="img" aria-label="Portrait du client"></div>
      <div>
        <p>Lorem ipsum dolor sit amet, ex vim ipsum primis. Sed quaestio molestiae ea duo, fabellas eleifend ut usu, ei labore feugiat vim. Nam principes perpetua ex, mea admodum praesent et. Vel ea graeci labitur.</p>
        <cite>Paul Martin</cite>
      </div>
    </div>
    <div class="dots"><span class="on"></span><span></span><span></span></div>
  </div>
  <div class="figures">
    <h3>Quelques Chiffres</h3>
    <p>Lorem ipsum dolor sit amet, ex vim ipsum primis. Sed quaestio molestiae ea duo, fabellas eleifend ut usu.</p>
    <div class="counter"><span>9</span><span>8</span><span>8</span><span>2</span><span>5</span><span>7</span><span>9</span><span>7</span><span>6</span><span>5</span></div>
    <div class="counter"><span>9</span><span>8</span><span>8</span><span>2</span><span>5</span><span>7</span><span>9</span><span>7</span><span>6</span><span>5</span></div>
  </div>
</section>

<footer class="footer">
  <div class="footer-about">
    <h3 class="title">Vendre En Vue De Racheter</h3>
    <p>Lorem ipsum dolor sit amet, ex vim ipsum primis. Sed quaestio molestiae ea duo, fabellas eleifend ut usu, ei labore feugiat vim. Nam principes perpetua ex, mea admodum praesent et. Vel ea graeci labitur, ne duo dicta iudico. Ius ut tota volumus, at cum viris vocent.</p>
  </div>
  <ul class="footer-links">
    <li>Accueil</li><li>Concept</li><li>Les Biens</li><li>Estimations</li><li>FAQ</li><li>Qui Sommes Nous ?</li><li>Mon Compte</li><li>Vendre &amp; Biens</li><li>Rachat De Biens</li>
  </ul>
  <div class="footer-contact">
    <svg width="18" height="24" viewBox="0 0 18 24"><path d="M9 0C4 0 0 4 0 9c0 6 9 15 9 15s9-9 9-15c0-5-4-9-9-9Z" fill="#f78f20"/><circle cx="9" cy="9" r="3" fill="#0c0c0c"/></svg>
    <p>Lumen Loans SAS<br>12 rue des Lilas, 75000 Paris<br>Tél : 01 23 45 67 89<br>Inscrite au registre du commerce de Paris<br>sous le numéro 000 000 000</p>
  </div>
  <div class="brand">Lumen Loans</div>
  <div class="copyright">Copyright 2015 Lumen Loans - All Rights Reserved</div>
</footer>

</body>
</html>
```